Borlavex Management

We need a web design for a new consulting company, with clients all over the world. The company provides management consulting to the travel industry.

Logo files are attached.

Website must look very corporate and be responsive in design.

Management Consulting

```html
<!DOCTYPE html>
<html lang="en">
<head>
<meta charset="utf-8">
<title>Borlavex Strategy Management, Inc.</title>
<link rel="stylesheet" href="https://fonts.googleapis.com/css2?family=Noto+Serif:ital,wght@0,400;0,700;1,400&display=swap">
<style>
:root{
  --navy:#0b1030;
  --navy-deep:#03071c;
  --green:#5fbf2a;
  --green-light:#7fd23f;
  --green-dark:#4aa51d;
  --text:#6e6e6e;
  --heading:#666;
  --band:#e4e4e4;
  --page:#f0f0f0;
  --white:#fff;
  --field:#e2e2e2;
  --slider-a:#0a3a8a;
  --slider-b:#1f7fe0;
}
*{box-sizing:border-box;margin:0;padding:0}
html,body{width:1200px;height:2257px;overflow:hidden}
body{position:relative;background:var(--page);font-family:"Noto Serif",Georgia,serif;color:var(--text)}
.abs{position:absolute}
.header{left:0;top:0;width:1200px;height:128px;background:var(--white)}
.brand{left:100px;top:28px;display:flex;align-items:center;gap:12px}
.brand-mark{width:48px;height:48px;border-radius:50%;background:var(--green)}
.brand-name{font-size:34px;font-weight:700;color:var(--navy);line-height:1}
.brand-sub{font-size:13px;font-weight:700;color:var(--navy);letter-spacing:1px;margin-top:4px}
.search{left:662px;top:36px;display:flex}
.search-input{width:150px;height:32px;border:1px solid #d4d4d4;border-right:0;font-style:italic;font-size:15px;color:#aaa;padding:6px 10px}
.search-btn{width:78px;height:32px;background:var(--green);color:var(--white);font-size:16px;text-align:center;line-height:32px}
.social{left:905px;top:34px;display:flex;gap:12px}
.social span{width:34px;height:34px;background:#9aa3b5;display:block}
.hero-band{left:0;top:128px;width:1200px;height:611px;background:var(--band)}
.nav{left:100px;top:109px;width:1002px;height:41px;background:var(--navy);display:flex;box-shadow:0 2px 4px rgba(0,0,0,.3)}
.nav a{flex:1;color:var(--white);text-decoration:none;font-size:21px;text-align:center;line-height:41px;border-left:1px solid #2c3355}
.nav a:first-child{border-left:0;flex:0 0 116px;background:linear-gradient(var(--green-light),var(--green-dark))}
.slide{left:100px;top:179px;width:1002px;height:472px;border:3px solid var(--white);background:radial-gradient(ellipse at 50% 45%,var(--slider-b),var(--slider-a) 70%,#061a45);box-shadow:0 14px 14px -8px rgba(0,0,0,.45)}
.arrow{top:389px;width:50px;height:53px;background:linear-gradient(var(--green-light),var(--green-dark))}
.arrow svg{display:block;margin:14px auto}
.arrow.prev{left:75px}.arrow.next{left:1076px}
.dots{left:555px;top:673px;display:flex;gap:12px}
.dots span{width:11px;height:11px;border-radius:50%;background:var(--green)}
.dots span:first-child{background:var(--white);border:2px solid var(--green)}
.welcome{left:301px;top:711px;width:600px;height:53px;background:var(--navy);color:var(--white);font-style:italic;font-size:26px;text-align:center;line-height:53px}
.card{top:796px;width:308px}
.card-photo{height:173px;border:3px solid #cfcfcf;background:linear-gradient(#c9ced6,#8d98a8)}
.card h2,.col h2{font-size:21px;font-weight:700;color:var(--heading);margin:16px 0 6px}
.card p,.col p{font-size:17px;line-height:23.5px}
.btn{display:inline-block;background:linear-gradient(var(--green-light),var(--green-dark));color:var(--white);font-weight:700;font-size:20px;text-align:center;height:38px;line-height:38px;width:137px}
.card .btn{margin-top:22px}
.quote-band{left:0;top:1241px;width:1200px;height:267px;background:var(--band)}
.quote{left:158px;top:1301px;width:884px;font-style:italic;font-size:17px;line-height:24px;text-align:center;color:#7a7a7a}
.quote-btn{left:532px;top:1439px}
.col{left:100px;width:470px}
.contact h2{font-size:21px;font-weight:700;color:var(--heading)}
.form{left:651px;top:1584px;width:451px;height:316px;background:#e8e8e8;padding:15px 13px}
.field{height:36px;background:var(--field);margin-bottom:20px;font-style:italic;font-size:16px;color:#999;padding:8px 10px}
.field.area{height:121px}
.submit{left:651px;top:1920px}
.footer{left:0;top:2005px;width:1200px;height:252px;background:linear-gradient(var(--navy),var(--navy-deep))}
.fcol{top:2026px;font-size:17px;line-height:24px;color:#b7bccb}
.fcol h3{color:var(--green-light);font-size:21px;font-weight:700;margin-bottom:10px}
.map{left:651px;top:2031px;width:451px;height:147px;background:linear-gradient(135deg,#e8e4d8,#cfdcc2 60%,#d7d2c6)}
.copy{top:2220px;font-size:11px;color:#8d92a4}
</style>
</head>
<body>
<header class="abs header"></header>
<div class="abs brand">
  <span class="brand-mark"></span>
  <div><div class="brand-name">BORLAVEX</div><div class="brand-sub">STRATEGY MANAGEMENT, INC.</div></div>
</div>
<div class="abs search"><div class="search-input">Search</div><div class="search-btn">Find</div></div>
<div class="abs social"><span></span><span></span><span></span><span></span><span></span></div>

<div class="abs hero-band"></div>
<nav class="abs nav"><a href="#">Home</a><a href="#">About</a><a href="#">Services</a><a href="#">Clients</a><a href="#">FAQs</a><a href="#">Blog</a><a href="#">Contact us</a></nav>
<div class="abs slide" role="img" aria-label="Businesswoman touching floating screens over a glowing world map"></div>
<div class="abs arrow prev"><svg width="20" height="24"><path d="M18 2 L3 12 L18 22Z" fill="#fff"/></svg></div>
<div class="abs arrow next"><svg width="20" height="24"><path d="M2 2 L17 12 L2 22Z" fill="#fff"/></svg></div>
<div class="abs dots"><span></span><span></span><span></span><span></span><span></span></div>
<div class="abs welcome">Welcome to Borlavex Strategy Management, Inc</div>

<div class="abs card" style="left:100px">
  <div class="card-photo" role="img" aria-label="Businessman smiling at his desk"></div>
  <h2>Lorem Ipsum</h2>
  <p>Lorem Ipsum is simply dummy text of the printing and typesetting industry. Lorem Ipsum has been the industry's standard dummy text ever since the 1500s, when an unknown printer took a galley of type and scrambled...</p>
  <span class="btn">Read more</span>
</div>
<div class="abs card" style="left:446px">
  <div class="card-photo" role="img" aria-label="Team of business people standing together"></div>
  <h2>Lorem Ipsum</h2>
  <p>Lorem Ipsum is simply dummy text of the printing and typesetting industry. Lorem Ipsum has been the industry's standard dummy text ever since the 1500s, when an unknown printer took a galley of type and scrambled...</p>
  <span class="btn">Read more</span>
</div>
<div class="abs card" style="left:792px">
  <div class="card-photo" role="img" aria-label="Clients shaking hands with a consultant"></div>
  <h2>Lorem Ipsum</h2>
  <p>Lorem Ipsum is simply dummy text of the printing and typesetting industry. Lorem Ipsum has been the industry's standard dummy text ever since the 1500s, when an unknown printer took a galley of type and scrambled...</p>
  <span class="btn">Read more</span>
</div>

<div class="abs quote-band"></div>
<p class="abs quote">Lorem Ipsum is simply dummy text of the printing and typesetting industry. Lorem Ipsum has been the industry's standard dummy text ever since the 1500s, when an unknown printer took a galley of type and scrambled it to make a type specimen book. It has survived not only five centuries, but also the leap into electronic typesetting, remaining essentially unchanged. It was popularised in the 1960s ...</p>
<span class="abs btn quote-btn">Read more</span>

<div class="abs col" style="top:1536px">
  <h2>Lorem Ipsum</h2>
  <p>Lorem Ipsum is simply dummy text of the printing and typesetting industry. Lorem Ipsum has been the industry's standard dummy text ever since the 1500s, when an unknown printer took a galley of type and scrambled<br>is simply dummy text of the printing and<br>is simply dummy text of the printing and...</p>
</div>
<div class="abs col" style="top:1773px">
  <h2>Lorem Ipsum</h2>
  <p>Lorem Ipsum is simply dummy text of the printing and typesetting industry. Lorem Ipsum has been the industry's standard dummy text ever since the 1500s, when an unknown printer took a galley of type and scrambled<br>is simply dummy text of the printing and<br>is simply dummy text of the printing and...</p>
</div>
<div class="abs contact" style="left:651px;top:1546px"><h2>Quick contact</h2></div>
<form class="abs form">
  <div class="field">Name</div><div class="field">Email</div><div class="field">Phone</div><div class="field area">Enquiry</div>
</form>
<span class="abs btn submit">Submit</span>

<footer class="abs footer"></footer>
<div class="abs fcol" style="left:100px"><h3>Find us</h3>Address line one<br>Address line two<br>Address line three<br>Address line four<br>Address line five</div>
<div class="abs fcol" style="left:352px"><h3>Contact</h3>01234 567890<br>07779 123456<br>07779 123456<br>email@companyname.com<br>www.companyname.com</div>
<div class="abs map" role="img" aria-label="Street map showing the office location"></div>
<p class="abs copy" style="left:100px">Copyright © 2014 Example Corporation. All rights reserved.</p>
<p class="abs copy" style="left:900px;width:202px;text-align:right">Sitemap / Privacy Policy / Terms of use</p>
</body>
</html>
```